Brisk Tray Packs

Need a very simple diagonal random design on bag. using 2 colors only
Packaging material on a roll. 11' Wide total, do not need eye spot since it is random print.
Target Market(s)
hospitality industry
Colors
Designer to choose colors to be used in the design.
Requirements
Must have
- Open for design ideas very simple since it is repeat.the text should be diagonal.
- Need for whole bag to be black, the test can be in Gold.
- On the front of the bag:
- Lantern Roast Coffee
- 100% Arabica Coffee
- Back of the bag:
- This package contains one filter pack coffee and may
- also contain sugar, non-dairy creamer, sugar sub., and stirrer.
- Korvath & Sons Coffee
- Cedar Vale, TX 75710

```html
<!DOCTYPE html>
<html lang="en">
<head>
<meta charset="utf-8">
<title>Lantern Roast Coffee – Filter Pack Roll Layout</title>
<link rel="stylesheet" href="https://fonts.googleapis.com/css2?family=Arimo:wght@400&family=Bodoni+Moda:wght@400&family=Tinos:wght@400;700&display=swap">
<style>
  :root {
    --paper: #ffffff;
    --ink: #1a1a1a;
    --bag: #0c0c0c;
    --gold: #c9a24a;
    --gold-deep: #8a6a26;
  }
  html, body {
    margin: 0;
    padding: 0;
    width: 1200px;
    height: 991px;
    overflow: hidden;
    background: var(--paper);
  }
  .roll-sheet { display: block; width: 1200px; height: 991px; }

  .dim-label { font-family: "Arimo", Arial, sans-serif; font-size: 9px; fill: var(--ink); }
  .dim-small { font-family: "Arimo", Arial, sans-serif; font-size: 7px; fill: var(--ink); }
  .dim-tiny { font-family: "Arimo", Arial, sans-serif; font-size: 5px; fill: var(--ink); }
  .dim-line { stroke: var(--ink); stroke-width: 0.8; fill: none; }
  .bag-body { fill: var(--bag); }
  .guide-line { stroke: var(--gold); stroke-opacity: 0.45; stroke-width: 0.7; stroke-dasharray: 4 3; fill: none; }

  .repeat-text { font-family: "Tinos", "Times New Roman", serif; font-size: 28px; fill: var(--gold); fill-opacity: 0.16; letter-spacing: 2px; }

  .brand-name { font-family: "Bodoni Moda", "Didot", serif; fill: var(--gold); }
  .blend-band { fill: var(--gold); }
  .blend-name { font-family: "Tinos", "Times New Roman", serif; font-size: 15px; fill: var(--bag); }
  .blend-sub { font-family: "Tinos", "Times New Roman", serif; font-size: 7px; font-weight: 700; fill: var(--bag); letter-spacing: 0.3px; }
  .blend-rule { stroke: var(--bag); stroke-width: 0.6; stroke-dasharray: 1 1.5; }
  .roast-type { font-family: "Tinos", "Times New Roman", serif; font-size: 15px; fill: var(--gold); }
  .maker-line { font-family: "Tinos", "Times New Roman", serif; font-size: 6.5px; font-weight: 700; fill: var(--gold); }
  .back-copy { font-family: "Tinos", "Times New Roman", serif; font-size: 6.4px; fill: var(--gold); }
  .seal-badge { fill: var(--bag); stroke: var(--gold); stroke-width: 1.6; }
  .seal-badge-inner { fill: none; stroke: var(--gold); stroke-width: 0.8; }
  .roll-icon { fill: var(--paper); stroke: var(--ink); stroke-width: 0.8; }
  .roll-icon-text { font-family: "Arimo", Arial, sans-serif; font-size: 3.6px; fill: var(--ink); }
</style>
</head>
<body>
<svg class="roll-sheet" viewBox="0 0 1410 1165" xmlns="http://www.w3.org/2000/svg">
  <defs>
    <linearGradient id="gold-scene" x1="0" y1="0" x2="0" y2="1">
      <stop offset="0" stop-color="#c9a24a"/>
      <stop offset="1" stop-color="#8a6a26"/>
    </linearGradient>
    <marker id="arrow-end" viewBox="0 0 6 6" refX="6" refY="3" markerWidth="5" markerHeight="5" orient="auto">
      <path d="M0 0 L6 3 L0 6 Z" fill="#1a1a1a"/>
    </marker>
    <marker id="arrow-start" viewBox="0 0 6 6" refX="0" refY="3" markerWidth="5" markerHeight="5" orient="auto">
      <path d="M6 0 L0 3 L6 6 Z" fill="#1a1a1a"/>
    </marker>
    <clipPath id="bag-clip"><rect x="28" y="28" width="587" height="310"/></clipPath>

    <g id="bag-layout">
      <!-- web width dimension -->
      <line class="dim-line" x1="30" y1="12" x2="615" y2="12" marker-start="url(#arrow-start)" marker-end="url(#arrow-end)"/>
      <text class="dim-label" x="322" y="8" text-anchor="middle">WEB WIDTH 11"</text>
      <!-- cutoff dimension -->
      <line class="dim-line" x1="12" y1="28" x2="12" y2="338" marker-start="url(#arrow-start)" marker-end="url(#arrow-end)"/>
      <text class="dim-label" transform="translate(8 183) rotate(-90)" text-anchor="middle">CUTOFF 5.8333"</text>

      <!-- black bag body -->
      <rect class="bag-body" x="28" y="28" width="587" height="310"/>

      <!-- diagonal gold repeat print -->
      <g clip-path="url(#bag-clip)">
        <g transform="rotate(-30 321 183)">
          <text class="repeat-text" x="-240" y="-110">LANTERN ROAST COFFEE · 100% ARABICA COFFEE · LANTERN ROAST COFFEE</text>
          <text class="repeat-text" x="-300" y="-50">KORVATH &amp; SONS COFFEE · CEDAR VALE, TX 75710 · KORVATH &amp; SONS</text>
          <text class="repeat-text" x="-260" y="10">LANTERN ROAST COFFEE · 100% ARABICA COFFEE · LANTERN ROAST COFFEE</text>
          <text class="repeat-text" x="-320" y="70">KORVATH &amp; SONS COFFEE · CEDAR VALE, TX 75710 · KORVATH &amp; SONS</text>
          <text class="repeat-text" x="-280" y="130">LANTERN ROAST COFFEE · 100% ARABICA COFFEE · LANTERN ROAST COFFEE</text>
          <text class="repeat-text" x="-340" y="190">KORVATH &amp; SONS COFFEE · CEDAR VALE, TX 75710 · KORVATH &amp; SONS</text>
          <text class="repeat-text" x="-300" y="250">LANTERN ROAST COFFEE · 100% ARABICA COFFEE · LANTERN ROAST COFFEE</text>
          <text class="repeat-text" x="-360" y="310">KORVATH &amp; SONS COFFEE · CEDAR VALE, TX 75710 · KORVATH &amp; SONS</text>
          <text class="repeat-text" x="-320" y="370">LANTERN ROAST COFFEE · 100% ARABICA COFFEE · LANTERN ROAST COFFEE</text>
          <text class="repeat-text" x="-380" y="430">KORVATH &amp; SONS COFFEE · CEDAR VALE, TX 75710 · KORVATH &amp; SONS</text>
          <text class="repeat-text" x="-340" y="490">LANTERN ROAST COFFEE · 100% ARABICA COFFEE · LANTERN ROAST COFFEE</text>
        </g>
      </g>

      <!-- fold guides -->
      <line class="guide-line" x1="28" y1="46" x2="615" y2="46"/>
      <line class="guide-line" x1="28" y1="316" x2="615" y2="316"/>
      <line class="guide-line" x1="83" y1="28" x2="83" y2="338"/>
      <line class="guide-line" x1="189" y1="28" x2="189" y2="338"/>
      <line class="guide-line" x1="456" y1="28" x2="456" y2="338"/>
      <line class="guide-line" x1="562" y1="28" x2="562" y2="338"/>

      <!-- scenic band -->
      <g role="img" aria-label="Gold-toned panorama of a canal city skyline with a domed basilica and moored gondolas">
        <rect x="28" y="30" width="537" height="142" fill="url(#gold-scene)"/>
      </g>

      <!-- seal dimensions -->
      <line class="dim-line" x1="672" y1="28" x2="672" y2="46" marker-start="url(#arrow-start)" marker-end="url(#arrow-end)"/>
      <text class="dim-small" transform="translate(644 26) rotate(90)">0.375"</text>
      <text class="dim-small" transform="translate(654 28) rotate(90)">SEAL</text>
      <line class="dim-line" x1="672" y1="316" x2="672" y2="338" marker-start="url(#arrow-start)" marker-end="url(#arrow-end)"/>
      <text class="dim-small" transform="translate(644 314) rotate(90)">0.375"</text>
      <text class="dim-small" transform="translate(654 316) rotate(90)">SEAL</text>

      <!-- unwind icon -->
      <g transform="translate(658 234) rotate(12)">
        <rect class="roll-icon" x="0" y="0" width="34" height="14" rx="2"/>
        <circle class="roll-icon" cx="3" cy="7" r="3"/>
        <text class="roll-icon-text" x="9" y="6">PRESS</text>
        <text class="roll-icon-text" x="9" y="11">THIS WAY</text>
      </g>
      <line class="dim-line" x1="675" y1="260" x2="675" y2="279" marker-end="url(#arrow-end)"/>
      <text class="dim-tiny" x="673" y="288" text-anchor="middle">#2 Unwind</text>
      <text class="dim-tiny" x="673" y="294" text-anchor="middle">with 3" core</text>

      <!-- panel width dimensions -->
      <line class="dim-line" x1="30" y1="372" x2="615" y2="372"/>
      <line class="dim-line" x1="30" y1="340" x2="30" y2="378"/>
      <line class="dim-line" x1="83" y1="340" x2="83" y2="378"/>
      <line class="dim-line" x1="189" y1="340" x2="189" y2="378"/>
      <line class="dim-line" x1="456" y1="340" x2="456" y2="378"/>
      <line class="dim-line" x1="562" y1="340" x2="562" y2="378"/>
      <line class="dim-line" x1="615" y1="340" x2="615" y2="378"/>
      <text class="dim-label" x="56" y="353" text-anchor="middle">1"</text>
      <text class="dim-label" x="56" y="366" text-anchor="middle">SEAL</text>
      <text class="dim-label" x="136" y="368" text-anchor="middle">2"</text>
      <text class="dim-label" x="322" y="368" text-anchor="middle">FACE 5"</text>
      <text class="dim-label" x="508" y="368" text-anchor="middle">2"</text>
      <text class="dim-label" x="588" y="353" text-anchor="middle">1"</text>
      <text class="dim-label" x="588" y="366" text-anchor="middle">SEAL</text>

      <!-- left gusset: maker block -->
      <text class="brand-name" x="136" y="216" font-size="15" text-anchor="middle">Caffè Lumino</text>
      <circle class="seal-badge" cx="137" cy="255" r="27"/>
      <circle class="seal-badge-inner" cx="137" cy="255" r="19"/>
      <text class="maker-line" x="137" y="294" text-anchor="middle">Korvath &amp; Sons Coffee</text>
      <text class="maker-line" x="137" y="302" text-anchor="middle">Cedar Vale, TX 75710</text>

      <!-- face -->
      <text class="brand-name" x="230" y="226" font-size="30">Caffè Lumino</text>
      <rect class="blend-band" x="160" y="238" width="222" height="39"/>
      <text class="blend-name" x="230" y="258">LANTERN ROAST</text>
      <line class="blend-rule" x1="230" y1="263" x2="350" y2="263"/>
      <text class="blend-sub" x="232" y="273">100% ARABICA COFFEE</text>
      <text class="roast-type" x="230" y="292">REGULAR</text>
      <circle class="seal-badge" cx="388" cy="257" r="34"/>
      <circle class="seal-badge-inner" cx="388" cy="257" r="24"/>

      <!-- right gusset: back copy -->
      <g transform="translate(485 296) rotate(-90)">
        <text class="back-copy" x="0" y="0">This package contains one filter pack</text>
        <text class="back-copy" x="0" y="8">coffee and may also contain sugar,</text>
        <text class="back-copy" x="0" y="16">non-dairy creamer, sugar sub., and stirrer.</text>
      </g>
    </g>
  </defs>

  <!-- six bag layouts -->
  <use href="#bag-layout" x="0" y="0"/>
  <use href="#bag-layout" x="709" y="0"/>
  <use href="#bag-layout" x="0" y="390"/>
  <use href="#bag-layout" x="709" y="390"/>
  <use href="#bag-layout" x="0" y="780"/>
  <use href="#bag-layout" x="709" y="780"/>
</svg>
</body>
</html>
```